we are starting an online childrens clothing store, The Otter And The Kite, and require an easy to navigate, simple and elegant in design. we will suply our own domain and company logo.

Target Market(s)

Familys with children aged 0 to 8

Industry/Entity Type

Clothing

Requirements
Must have
• easy to navigate,
our company logo on the header of each page
easy two step checkout with coinrill access.
easy to modify and add to site by us at no or minimal cost.
6 pages, home page, boys clothing, girls clothing, our brands, about us, contact.
brightmark ads
kin wall link
Should not have
• pop up ads
dark colours

```html
<!DOCTYPE html>
<html lang="en">
<head>
<meta charset="utf-8">
<title>The Otter And The Kite – Children's Clothing</title>
<link rel="stylesheet" href="https://fonts.googleapis.com/css2?family=Cinzel:wght@400&family=Roboto:wght@100;300;400;500;700&display=swap">
<style>
:root{
  --red:#c0272d;
  --red-dark:#a82228;
  --plum:#3d3135;
  --plum-deep:#342a2d;
  --sand-light:#ece5cf;
  --sand-dark:#c9bc94;
  --nav-text:#5b4a3e;
  --grey-text:#6a6a6a;
  --light-bg:#f6f6f6;
  --white:#ffffff;
  --footer-text:#e4dcdf;
}
*{box-sizing:border-box;margin:0;padding:0}
html,body{width:803px;height:1200px;overflow:hidden}
body{position:relative;background:var(--light-bg);font-family:'Roboto',sans-serif;color:var(--grey-text)}
.abs{position:absolute}

.top-bar{left:0;top:0;width:803px;height:31px;background:var(--red)}
.top-links{right:164px;top:11px;font-size:10px;color:var(--white)}
.sign-in{left:662px;top:7px;width:60px;height:18px;background:#b32228;color:var(--white);font-size:10px;text-align:center;line-height:18px}

.header{left:0;top:31px;width:803px;height:93px;background:var(--plum)}
.logo-mark{left:118px;top:42px;width:36px;height:36px;border:1.5px solid #cfc3b7;border-radius:50%}
.logo-name{left:92px;top:83px;width:125px;font-family:'Cinzel',serif;font-size:13px;line-height:14px;color:#cfc3b7;text-align:center}
.cart{left:567px;top:53px}
.cart-text{left:608px;top:61px;font-size:12px;font-weight:300;color:#d7cfd2}
.search{left:501px;top:88px;width:149px;height:19px;background:var(--white);font-size:8px;color:#222;padding:5px 6px}
.search-btn{left:654px;top:88px;width:62px;height:19px;background:var(--red);color:var(--white);font-size:8px;text-align:center;line-height:19px}

.nav{left:0;top:124px;width:803px;height:44px;background:linear-gradient(var(--sand-light),var(--sand-dark))}
.nav ul{list-style:none;display:flex;position:absolute;left:90px;top:0;height:44px}
.nav li{font-family:'Cinzel',serif;font-size:13px;color:var(--nav-text);line-height:44px;padding:0 15px 0 16px;border-left:1px solid rgba(255,255,255,.45)}
.nav li:first-child{border-left:none}

.hero-photo{left:82px;top:175px;width:429px;height:275px;background:linear-gradient(135deg,#6b5d5a 0%,#3a2f30 45%,#8a6e70 75%,#c14a4e 100%)}
.hero-offer{left:511px;top:175px;width:213px;height:275px;background:var(--red);color:var(--white);text-align:center}
.offer-1{left:0;width:213px;top:30px;font-size:28px;font-weight:300;letter-spacing:.5px}
.offer-2{left:0;width:213px;top:60px;font-size:68px;font-weight:100;line-height:72px}
.offer-3{left:0;width:213px;top:124px;font-size:58px;font-weight:700;line-height:60px}
.shop-now{left:38px;top:199px;width:138px;height:40px;background:var(--plum);font-size:20px;font-weight:300;line-height:40px}
.dots{left:457px;top:428px}

.feature{font-size:14px;line-height:19px;font-weight:300;color:#555}
.feature b{font-weight:500;color:var(--red);display:block}
.shadow{height:6px;width:72px;border-radius:50%;background:radial-gradient(rgba(0,0,0,.14),transparent 70%)}

.section-title{left:0;width:803px;top:560px;text-align:center;font-size:16px;color:var(--red)}
.product .img{position:absolute;left:0;top:0;width:147px;height:124px;border:1px solid #e2e2e2}
.product .name{position:absolute;left:0;top:131px;font-size:9px;white-space:nowrap}
.product .price{position:absolute;left:0;top:146px;font-size:19px;color:#555}
.product .btn{position:absolute;left:0;top:176px;width:62px;height:19px;background:var(--red);color:var(--white);font-size:9px;text-align:center;line-height:19px}

.newsletter{left:0;top:806px;width:803px;height:194px;background:var(--white)}
.nl-title{left:92px;top:20px;font-size:21px;color:#555;font-weight:300}
.nl-title span{color:var(--red);font-weight:400}
.nl-text{left:91px;top:60px;width:400px;font-size:8.5px;line-height:20px;font-weight:300;color:#777}
.nl-input{left:87px;top:99px;width:414px;height:31px;background:#f1f1f1}
.nl-btn{left:86px;top:137px;width:79px;height:28px;background:var(--red);color:var(--white);font-size:13px;text-align:center;line-height:28px;border:1px solid var(--red-dark)}
.ad{left:517px;top:15px;width:201px;height:167px;background:linear-gradient(#3d9a3a,#2e7b2d);border:2px solid #22552a}

.footer{left:0;top:1000px;width:803px;height:156px;background:var(--plum)}
.footer h4{position:absolute;top:23px;font-size:9px;font-weight:400;color:var(--footer-text)}
.footer ul{position:absolute;top:54px;list-style:none;font-size:9.5px;line-height:16px;color:var(--footer-text)}
.social li{display:flex;align-items:center;justify-content:space-between;width:98px;height:25px}
.social i{display:block;width:14px;height:14px;border-radius:50%;background:var(--white)}
.bottom-bar{left:0;top:1156px;width:803px;height:44px;background:var(--plum-deep);border-top:1px solid #4a3d41}
.copyright{left:86px;top:17px;font-size:9.5px;color:var(--footer-text)}
</style>
</head>
<body>

<div class="abs top-bar"></div>
<div class="abs top-links">My Account &nbsp;| &nbsp;Help &nbsp;| &nbsp;Checkout</div>
<div class="abs sign-in">Sign In</div>

<header class="abs header"></header>
<div class="abs logo-mark"></div>
<div class="abs logo-name">The Otter And<br>The Kite</div>
<svg class="abs cart" width="36" height="26" viewBox="0 0 36 26" aria-hidden="true">
  <path d="M3 7 L33 7 L29 22 L7 22 Z" fill="#f2b915"/>
  <path d="M8 7 L13 1 M28 7 L23 1" stroke="#f2b915" stroke-width="2"/>
  <path d="M10 10v9M15 10v9M20 10v9M25 10v9" stroke="#c88d0a" stroke-width="1.5"/>
</svg>
<div class="abs cart-text">Add to Cart (0 Items)</div>
<div class="abs search">Search</div>
<div class="abs search-btn">SEARCH</div>

<nav class="abs nav">
  <ul>
    <li>Home</li><li>Boys Clothing</li><li>Girls Clothing</li><li>Our Brands</li><li>About Us</li><li>Contact</li>
  </ul>
</nav>

<div class="abs hero-photo" role="img" aria-label="Shop window with children's clothing on display and a new arrivals sign"></div>
<div class="abs hero-offer">
  <div class="abs offer-1">GREAT SALE</div>
  <div class="abs offer-2">45%</div>
  <div class="abs offer-3">FLAT</div>
  <div class="abs shop-now">SHOP NOW</div>
</div>
<svg class="abs dots" width="46" height="12" aria-hidden="true">
  <circle cx="5" cy="6" r="4.5" fill="#c0272d"/><circle cx="17" cy="6" r="4.5" fill="#fff"/>
  <circle cx="29" cy="6" r="4.5" fill="#fff"/><circle cx="41" cy="6" r="4.5" fill="#fff"/>
</svg>

<div class="abs feature" style="left:103px;top:488px"><b>FREE SHIPPING</b>ABOVE RS. 500</div>
<svg class="abs" style="left:226px;top:484px" width="38" height="44" viewBox="0 0 38 44" aria-hidden="true">
  <rect x="5" y="2" width="28" height="34" rx="4" fill="#3d3135"/>
  <rect x="9" y="7" width="20" height="11" fill="#fff"/>
  <rect x="1" y="14" width="4" height="8" fill="#3d3135"/><rect x="33" y="14" width="4" height="8" fill="#3d3135"/>
  <rect x="9" y="26" width="6" height="3" fill="#fff"/><rect x="23" y="26" width="6" height="3" fill="#fff"/>
  <rect x="8" y="36" width="6" height="6" fill="#3d3135"/><rect x="24" y="36" width="6" height="6" fill="#3d3135"/>
</svg>
<div class="abs shadow" style="left:214px;top:532px"></div>

<div class="abs feature" style="left:318px;top:488px"><b>CASH ON</b>DELIVERY</div>
<svg class="abs" style="left:440px;top:490px" width="44" height="32" viewBox="0 0 44 32" aria-hidden="true">
  <path d="M14 2h28M14 7h28M14 12h28M14 17h28M14 22h28M14 27h28" stroke="#3d3135" stroke-width="3"/>
  <circle cx="11" cy="20" r="10" fill="#3d3135"/>
  <text x="11" y="25" font-family="Roboto,sans-serif" font-size="13" font-weight="700" fill="#fff" text-anchor="middle">$</text>
</svg>
<div class="abs shadow" style="left:428px;top:532px"></div>

<div class="abs feature" style="left:532px;top:478px"><b>DISPATCH</b>WITHIN 24 HOURS<br>DELIVERY</div>
<svg class="abs" style="left:660px;top:486px" width="44" height="40" viewBox="0 0 44 40" aria-hidden="true">
  <rect x="4" y="1" width="36" height="30" rx="5" fill="#3d3135"/>
  <rect x="8" y="6" width="13" height="11" fill="#fff"/><rect x="23" y="6" width="13" height="11" fill="#fff"/>
  <rect x="0" y="8" width="4" height="8" fill="#3d3135"/><rect x="40" y="8" width="4" height="8" fill="#3d3135"/>
  <circle cx="12" cy="24" r="2.5" fill="#fff"/><circle cx="32" cy="24" r="2.5" fill="#fff"/>
  <rect x="8" y="31" width="6" height="7" fill="#3d3135"/><rect x="30" y="31" width="6" height="7" fill="#3d3135"/>
</svg>
<div class="abs shadow" style="left:650px;top:532px"></div>

<h2 class="abs section-title" style="font-weight:400">OUR FEATURED PRODUCTS</h2>

<div class="abs product" style="left:86px;top:595px">
  <div class="img" role="img" aria-label="Lime green zip jacket" style="background:linear-gradient(#eef0ea,#dfe6b0)"></div>
  <div class="name">Check Shirt With Mock Tee</div><div class="price">$34.50</div><div class="btn">ADD CART</div>
</div>
<div class="abs product" style="left:247px;top:595px">
  <div class="img" role="img" aria-label="Light blue ruffled skirt" style="background:linear-gradient(#f2f4f6,#8fc0e6)"></div>
  <div class="name">Check Shirt With Mock Tee</div><div class="price">$34.50</div><div class="btn">ADD CART</div>
</div>
<div class="abs product" style="left:408px;top:595px">
  <div class="img" role="img" aria-label="White and green long sleeve shirt" style="background:linear-gradient(#e8e8e8,#c9dd7a)"></div>
  <div class="name">Check Shirt With Mock Tee</div><div class="price">$34.50</div><div class="btn">ADD CART</div>
</div>
<div class="abs product" style="left:568px;top:595px">
  <div class="img" role="img" aria-label="Pink dress with floral skirt" style="background:linear-gradient(#eaeaea,#f0b8b0 55%,#4a3a3a)"></div>
  <div class="name">Check Shirt With Mock Tee</div><div class="price">$34.50</div><div class="btn">ADD CART</div>
</div>

<section class="abs newsletter">
  <h3 class="abs nl-title"><span>Sign Up</span> Newsletter</h3>
  <p class="abs nl-text">Lorem Ipsum is simply dummy text of the printing and typesetting industry. Lorem Ipsum has been the industry's</p>
  <div class="abs nl-input"></div>
  <div class="abs nl-btn">Subscribe</div>
  <div class="abs ad" role="img" aria-label="brightmark ads banner"></div>
</section>

<footer class="abs footer">
  <h4 style="left:85px">MENULINKS</h4>
  <ul style="left:85px"><li>Home</li><li>Boys Clothing</li><li>Girls Clothing</li><li>Our Brands</li><li>About Us</li><li>Contact</li></ul>
  <h4 style="left:224px">CUSTOMER SERVICE</h4>
  <ul style="left:224px"><li>How to shop</li><li>Delivery &amp; payment</li><li>Returns &amp; refunds</li><li>Safety &amp; privacy</li></ul>
  <h4 style="left:357px">CONTACT US</h4>
  <ul style="left:357px"><li>Lindgatan 14</li><li>S-612 40 Brenneby</li><li>P: + 46 (0) 150-418 36</li><li>M: shop@otterkite.com</li></ul>
  <h4 style="left:567px">CONNECT WITH US</h4>
  <ul class="social" style="left:567px;top:46px"><li>Chirpline<i></i></li><li>Kin Wall<i></i></li><li>Linkforge<i></i></li></ul>
</footer>
<div class="abs bottom-bar"><div class="abs copyright">Copyright ©2013 Company Name &nbsp;&nbsp;- All rights reserved</div></div>

</body>
</html>
```